A Label for an ECO Friendly Spirit Company

Design a label which can be used for vodka and gin (London Dry Gin). It should be Square type Like the Shape File you see in the uploads. VORK means Local Eco friendly Authentic and Fair. We want a cool and slim label that calls for eco-friendly. We want to use it for our premium
Vodka and our London Dry Gin. Please use the logo and design it in Square Type.

40%vol, 700ml

Target Market(s)

spirits and events

Industry/Entity Type

SPIRITS

Colors
00AB8E
00BBA5
67D7C9
C6EFE9
E9F9F6
59FF00
82FF00
B8FF75
E3FFCB
F4FFEA

Requirements
Must have
• Logo from VORK, Squaee Shape

```html
<!DOCTYPE html>
<html lang="en">
<head>
<meta charset="utf-8">
<title>VORK London Dry Gin Label</title>
<link rel="stylesheet" href="https://fonts.googleapis.com/css2?family=Sancreek&family=Rye&display=swap">
<style>
  :root {
    --paper-light: #eeedf1;
    --paper-dark: #e2e1e6;
    --label-white: #ffffff;
    --band-green: #8dc63f;
    --band-green-light: #b4dc7a;
    --label-teal: #00ab8e;
    --ornament-teal: #3cc0a8;
    --ornament-teal-soft: #67d7c9;
    --window-base: #ffffff;
    --window-stripe: #e3f2d3;
    --brand-green: #8dc63f;
  }
  html, body {
    margin: 0;
    padding: 0;
    width: 928px;
    height: 1200px;
    overflow: hidden;
  }
  body {
    background: linear-gradient(135deg, var(--paper-light), var(--paper-dark));
  }
  .label-canvas {
    display: block;
    width: 928px;
    height: 1200px;
  }
  .headline {
    font-family: "Sancreek", "Rye", serif;
    fill: var(--label-white);
  }
  .brand-name {
    font-family: "Sancreek", "Rye", serif;
    fill: var(--brand-green);
  }
  .volume-note {
    font-family: "Sancreek", "Rye", serif;
    fill: var(--label-teal);
    letter-spacing: 1px;
  }
  .speed-lines line {
    stroke: var(--label-white);
    stroke-width: 1.6;
  }
</style>
</head>
<body>
<svg class="label-canvas" viewBox="0 0 928 1200" xmlns="http://www.w3.org/2000/svg" aria-label="VORK London Dry Gin label">
  <defs>
    <pattern id="band-stripes" width="10" height="10" patternUnits="userSpaceOnUse" patternTransform="rotate(45)">
      <rect width="10" height="10" fill="var(--band-green)"/>
      <rect width="3" height="10" fill="var(--band-green-light)"/>
    </pattern>
    <pattern id="window-stripes" width="9" height="10" patternUnits="userSpaceOnUse">
      <rect width="9" height="10" fill="var(--window-base)"/>
      <rect width="4" height="10" fill="var(--window-stripe)"/>
    </pattern>
    <linearGradient id="ornament-fill" x1="0" y1="0" x2="0" y2="1">
      <stop offset="0" stop-color="var(--ornament-teal-soft)"/>
      <stop offset="1" stop-color="var(--ornament-teal)"/>
    </linearGradient>
    <clipPath id="window-clip">
      <circle cx="448" cy="642" r="198"/>
    </clipPath>
    <path id="ornament-zone" d="M448,280 L596,428 L588,502 A198 198 0 0 0 308,502 L300,428 Z"/>
  </defs>

  <!-- label frame -->
  <polygon class="label-edge" points="448,219 872,642 448,1066 25,642" fill="var(--label-white)"/>
  <polygon class="label-band" points="448,225 866,642 448,1059 33,642" fill="url(#band-stripes)"/>
  <polygon class="label-field" points="448,248 843,642 448,1036 55,642" fill="var(--label-teal)"/>

  <!-- filigree areas -->
  <g class="ornament-zones" role="img" aria-label="White swirling filigree ornament with small leaves filling the four corners of the label">
    <use href="#ornament-zone" fill="url(#ornament-fill)"/>
    <use href="#ornament-zone" fill="url(#ornament-fill)" transform="rotate(90 448 642)"/>
    <use href="#ornament-zone" fill="url(#ornament-fill)" transform="rotate(180 448 642)"/>
    <use href="#ornament-zone" fill="url(#ornament-fill)" transform="rotate(270 448 642)"/>
  </g>

  <!-- central striped window -->
  <g class="center-window" clip-path="url(#window-clip)">
    <rect x="250" y="444" width="396" height="396" fill="url(#window-stripes)"/>
    <rect class="title-band" x="240" y="595" width="420" height="190" fill="var(--label-teal)"/>
  </g>

  <!-- brand -->
  <text class="brand-name" x="448" y="540" font-size="44" text-anchor="middle">VORK</text>

  <!-- title -->
  <text class="headline" x="268" y="707" font-size="138" textLength="360" lengthAdjust="spacingAndGlyphs">LONDON</text>
  <text class="headline" x="312" y="764" font-size="84" textLength="271" lengthAdjust="spacingAndGlyphs">DRY GIN</text>

  <g class="speed-lines">
    <line x1="275" y1="712" x2="304" y2="704"/>
    <line x1="278" y1="720" x2="304" y2="713"/>
    <line x1="280" y1="728" x2="304" y2="722"/>
    <line x1="282" y1="736" x2="304" y2="731"/>
    <line x1="284" y1="744" x2="304" y2="740"/>
    <line x1="287" y1="752" x2="304" y2="749"/>
    <line x1="290" y1="760" x2="304" y2="758"/>
    <line x1="621" y1="712" x2="592" y2="704"/>
    <line x1="618" y1="720" x2="592" y2="713"/>
    <line x1="616" y1="728" x2="592" y2="722"/>
    <line x1="614" y1="736" x2="592" y2="731"/>
    <line x1="612" y1="744" x2="592" y2="740"/>
    <line x1="609" y1="752" x2="592" y2="749"/>
    <line x1="606" y1="760" x2="592" y2="758"/>
  </g>

  <text class="volume-note" x="448" y="815" font-size="17" text-anchor="middle">40%VOL, 700ML</text>
</svg>
</body>
</html>
```